Can you create a Business Card based on the Logo you designed.

See example and would like to see other examples.

Trying to keep it very clean with a focus on the logo and name.

```html
<!DOCTYPE html>
<html lang="en">
<head>
<meta charset="UTF-8">
<title>Verdanta Business Card</title>
<link href="https://fonts.googleapis.com/css2?family=Open+Sans:wght@400;700&display=swap" rel="stylesheet">
<style>
  :root {
    --backdrop: #d6d6d6;
    --card-white: #f2f2f2;
    --brand-dark: #0b6128;
    --brand-light: #4aa82a;
    --brand-orange: #e5881c;
    --brand-orange-deep: #c9661a;
    --ink: #1c1c1c;
  }
  * { box-sizing: border-box; margin: 0; padding: 0; }
  html, body {
    width: 1200px;
    height: 1051px;
    overflow: hidden;
    background: var(--backdrop);
    font-family: "Open Sans", Arial, sans-serif;
  }
  .sheet {
    position: relative;
    width: 1200px;
    height: 1051px;
    display: flex;
    align-items: center;
    justify-content: center;
    gap: 40px;
  }
  .card {
    width: 500px;
    height: 286px;
    border-bottom: 4px solid var(--brand-orange);
    box-shadow: 0 14px 30px rgba(0,0,0,0.18);
  }
  .card-front {
    background: var(--card-white);
    display: flex;
    align-items: center;
    padding: 0 30px 0 34px;
  }
  .brand {
    display: flex;
    align-items: center;
    gap: 10px;
    width: 210px;
  }
  .brand-dot {
    width: 22px;
    height: 22px;
    border-radius: 50%;
    background: var(--brand-orange);
    flex: none;
  }
  .brand-name {
    font-weight: 700;
    font-size: 38px;
    color: var(--brand-dark);
    letter-spacing: -0.5px;
  }
  .divider {
    width: 2px;
    height: 140px;
    background: var(--brand-dark);
    margin: 0 20px 0 14px;
  }
  .details { color: var(--ink); }
  .person-name {
    font-weight: 700;
    font-size: 19px;
    letter-spacing: 0.5px;
    text-transform: uppercase;
    line-height: 1.1;
  }
  .person-name .first { color: var(--brand-dark); }
  .person-name .last { color: var(--brand-light); }
  .person-title {
    font-size: 13.5px;
    margin-bottom: 14px;
  }
  .contact-list { list-style: none; }
  .contact-list li {
    display: flex;
    align-items: center;
    gap: 6px;
    font-size: 13.5px;
    line-height: 1.45;
  }
  .contact-list svg { width: 11px; height: 11px; flex: none; fill: var(--brand-dark); }
  .card-back {
    background: linear-gradient(135deg, var(--brand-orange-deep) 0%, var(--brand-orange) 55%, #eb9a3f 100%);
  }
</style>
</head>
<body>
  <main class="sheet">
    <section class="card card-front">
      <div class="brand">
        <span class="brand-dot"></span>
        <span class="brand-name">Verdanta</span>
      </div>
      <div class="divider"></div>
      <div class="details">
        <p class="person-name"><span class="first">Marlo</span> <span class="last">Keating</span></p>
        <p class="person-title">Chief Executive Officer</p>
        <ul class="contact-list">
          <li>
            <svg viewBox="0 0 24 24" aria-hidden="true"><path d="M6.6 10.8a15 15 0 0 0 6.6 6.6l2.2-2.2c.3-.3.7-.4 1-.2 1.1.4 2.3.6 3.6.6.6 0 1 .4 1 1V20c0 .6-.4 1-1 1A17 17 0 0 1 3 4c0-.6.4-1 1-1h3.5c.6 0 1 .4 1 1 0 1.3.2 2.5.6 3.6.1.3 0 .7-.2 1z"/></svg>
            +1 (555) 014-2279
          </li>
          <li>
            <svg viewBox="0 0 24 24" aria-hidden="true"><path d="M2 5h20v14H2zm2 2v.5l8 5 8-5V7l-8 5z"/></svg>
            ceo@verdanta.com
          </li>
          <li>
            <svg viewBox="0 0 24 24" aria-hidden="true"><circle cx="12" cy="12" r="10"/></svg>
            www.verdanta.com
          </li>
        </ul>
      </div>
    </section>
    <section class="card card-back" role="img" aria-label="Orange card back with an embossed repeating leaf pattern"></section>
  </main>
</body>
</html>
```